vermalo web design

- Company / Site Description
We are developing a website that will allow anyone in Europe to find in one click, cultural things to do (Exhibition, Museum, Monument, Zoo, Aquarium, Archaeological site…) with friends or family, and to organize the visit (book a ticket / a private visit, book a restaurant nearby…).

Examples
1. You're in London with your girlfriend, it's saturday 10 am, you have two hours to spend and you want to see an exhibition. We provide you in one click all the exhibition matching your location / time and date.

2. You're in Berlin with some friends, it's thursday night you want to go out, but you don't know what to do. We provide you a list of experience, you can select for instance "I want to be on top of the world", and we show you a list of venues matching the selected experience / date / time /location of your request.

- Brand name : Vermalo
- Activity : Cultural Leisure, cultural entertainment

- Target audience
Broad target will be between 20 and 55. Core target will be between 25 and 40. Most likely to live in a city and in Europe.

- Behaviours and preferences
Our user is under time constraint (few minutes to find and choose his visit), idea constraint (is not sure about what to do and see) and money constraint.
He wants to have an easy to use website, not cluttered with information, focussed on added value information. He wants to have a website which is modern, fun and elegant that he will deem as professional and trustworthy.

- Our expectations (Do’s and Don’t)
We want to move away from traditional design. We want some OUT OF THE BOX design. Think of a website design that will look like an app design.
We want to make an awesome / extra ordinary /remember-able design. The design must be so cool, that the user wants to come back to the site. In two words: THINK EXTRAORDINARY.
You can use photos to help the user understand functions. If you use photo, use creative commons license photo.
Avoid black colors

- Functional Requirements
We need Four pages:
1. Home Page (desktop and mobile version): it’s both the homepage and the assistant page. This page will allow the user to find in one click his visit (please refer to the pdf file Assistant home page). The page must be self-explanatory for a first time user.
2. Assistant result page (desktop version): it’s the page that display the results found by the assistant based on the criteria search (please refer to the pdf file mockup - Assistant result page)
3. Site / Event page (desktop version): it’s the page that display each result information (please refer to the pdf file mockup – Event / Site Page)
The pdf files list all the elements include in each page + gives you a mockup of each page (just to put in perspective the element required). You are completely free about the design.
We don’t have the logo yet. Use a dummy logo for your page design.
The selected winner can expect to work with us immediately after the contest and on a on a regular basis later on.

- Technical Requirements
No Flash
For the winner, we will manage the CSS you will just need to provide :
. One PSD file containing all the pages
. Inside the PSD file we want for each page two groups: the first group will embed the desktop design, the second group will embed the responsive mobile design (Home Page only).
In total there should be 4 groups inside the PSD file (3 desktop groups, 1 mobile group).
Each group must contain all the elements specified in the pdf file

Website we like
http://demo.plandorix.example/?theme=Velunt
http://rosabel.quintorhub.example/#home
http://blogsite.fenk.daltoroute.example/2/
http://demo.plandorix.example/?theme=Mosaru
http://www.quarnivo.example/themes/lumbe/
http://gridmarket.example/item/tav-responsive-photography-blog-theme/full_screen_preview/8146027
http://items.zkvortel.example/?product=example
http://uk.harnoway.example

Reason: Due to the request of several designers, we have agreed to add 7 additional days to the contest deadline. Thank you. The vermalo team

Reason: We still need to collect all the votes. Sorry for the delay.

Reason: Hello, We extend the contest deadline, in order to collect all the votes from the poll. We should have everything finalized by sunday. Thank you vermalo team

```html
<!DOCTYPE html>
<html lang="en">
<head>
<meta charset="utf-8">
<title>Vermalo — Find in one click</title>
<link href="https://fonts.googleapis.com/css2?family=Questrial&display=swap" rel="stylesheet">
<style>
  :root{
    --stage:#3d3d3d;
    --green:#12c75a;
    --green-dark:#0fa94c;
    --header:#e4dcdc;
    --toolbar:#e9ebec;
    --white:#ffffff;
    --ink:#333333;
    --ink-soft:#555555;
    --muted:#9a9a9a;
    --go:#f1dfdf;
    --strip:#dedede;
    --footer:#b4b4b4;
    --label-band:rgba(30,30,30,.72);
    --sun:#f5e52a;
  }
  *{box-sizing:border-box;margin:0;padding:0}
  html,body{width:768px;height:1200px;overflow:hidden;background:var(--stage)}
  body{font-family:"Questrial",sans-serif;color:var(--ink);position:relative}

  .screen{position:absolute;left:48px;top:4px;width:672px;height:1193px;background:var(--white);overflow:hidden}

  /* Header */
  .site-header{position:absolute;left:0;top:0;width:672px;height:143px;background:var(--header)}
  .menu-toggle{position:absolute;left:0;top:0;width:60px;height:59px;background:var(--green);display:flex;flex-direction:column;justify-content:center;align-items:center;gap:6px}
  .menu-toggle span{display:block;width:38px;height:4px;background:var(--white)}
  .brand{position:absolute;left:0;right:0;top:72px;text-align:center;font-size:28px;letter-spacing:1px;color:var(--ink)}
  .brand-mark{position:absolute;left:50%;top:20px;width:44px;height:44px;margin-left:-22px;border:3px solid var(--green);border-radius:50%}

  /* Toolbar */
  .toolbar{position:absolute;left:0;top:143px;width:672px;height:84px;background:var(--toolbar)}
  .search{position:absolute;left:11px;top:24px;width:182px;height:41px;background:var(--white);border:1px solid #dcdcdc;font-size:16px;color:var(--muted);padding:12px 0 0 12px}
  .search svg{position:absolute;right:8px;top:7px}
  .welcome{position:absolute;right:104px;top:33px;font-size:15px;color:var(--ink)}
  .welcome b{font-weight:normal;color:var(--green);margin-left:6px}
  .avatar{position:absolute;left:588px;top:20px;width:49px;height:45px;background:var(--white);border:1px solid #dcdcdc}
  .avatar svg{position:absolute;left:14px;top:12px}
  .caret{position:absolute;left:651px;top:40px;border-left:6px solid transparent;border-right:6px solid transparent;border-top:6px solid #b8b8b8}

  /* Category strip */
  .categories{position:absolute;left:0;top:227px;width:672px;height:238px;display:flex}
  .category{position:relative;width:134.4px;height:238px}
  .category-label{position:absolute;left:0;right:0;bottom:0;height:46px;background:var(--label-band);color:var(--white);font-size:15px;text-align:center;line-height:46px}
  .cat-zoo{background:linear-gradient(160deg,#c9802f 0%,#e4b27a 40%,#3b2a1c 100%)}
  .cat-exhibition{background:linear-gradient(180deg,#1c120c 0%,#8a5a2c 45%,#c98f4c 70%,#3a2414 100%)}
  .cat-museum{background:linear-gradient(180deg,#2a1c10 0%,#b8862e 35%,#9a6a22 70%,#3a2a18 100%)}
  .cat-monuments{background:linear-gradient(180deg,#9cb6d0 0%,#d6e0ea 45%,#8c969e 100%)}
  .cat-parks{background:linear-gradient(180deg,#2e3a22 0%,#6d8a4c 40%,#a0a89a 75%,#5a6450 100%)}
  .slide-arrow{position:absolute;top:110px}
  .slide-arrow.prev{left:18px}
  .slide-arrow.next{right:18px}

  /* Assistant */
  .assistant{position:absolute;left:0;top:465px;width:672px;height:627px;text-align:center}
  .assistant h1{position:absolute;left:0;right:0;top:30px;font-weight:normal;font-size:34px;letter-spacing:1px;color:var(--green)}
  .weather{position:absolute;left:574px;top:34px;font-size:20px;color:var(--ink);display:flex;align-items:center;gap:4px}
  .intro{position:absolute;left:0;right:0;font-size:15px;color:var(--ink-soft);letter-spacing:.5px}
  .intro.one{top:89px}
  .intro.two{top:131px}
  .criteria{position:absolute;left:0;top:178px;width:672px}
  .criterion{position:absolute;display:flex;align-items:center;gap:12px;color:var(--green);white-space:nowrap}
  .criterion .value{font-size:28px}
  .criterion small{font-size:15px;margin-left:8px}
  .c-date{left:160px;top:12px}
  .c-time{left:160px;top:78px}
  .c-place{left:164px;top:144px}
  .cta{position:absolute;left:188px;top:410px;width:295px;height:73px;background:var(--green);color:var(--white);font-size:27px;line-height:73px;text-align:center;border-bottom:2px solid var(--green-dark)}
  .go{position:absolute;left:295px;top:517px;width:80px;height:80px;border-radius:50%;background:var(--go);color:var(--green);font-size:26px;line-height:80px;text-align:center}

  /* Footer */
  .more-strip{position:absolute;left:0;top:1092px;width:672px;height:39px;background:var(--strip);font-size:12px;color:var(--ink)}
  .more-strip span{position:absolute;right:16px;top:12px;display:flex;align-items:center;gap:10px}
  .more-strip i{display:block;border-left:6px solid transparent;border-right:6px solid transparent;border-bottom:8px solid var(--ink)}
  .site-footer{position:absolute;left:0;top:1131px;width:672px;height:62px;background:var(--footer);color:var(--white);font-size:16px;text-align:center;line-height:62px;letter-spacing:.5px}
</style>
</head>
<body>
<main class="screen">
  <header class="site-header">
    <div class="menu-toggle" aria-label="Menu"><span></span><span></span><span></span></div>
    <div class="brand-mark"></div>
    <div class="brand">VERMALO</div>
  </header>

  <div class="toolbar">
    <div class="search">Search
      <svg width="26" height="26" viewBox="0 0 26 26" fill="none" stroke="#888" stroke-width="1.6"><circle cx="16" cy="10" r="7"/><line x1="11" y1="15" x2="3" y2="23"/></svg>
    </div>
    <div class="welcome">Welcome<b>Loriane</b></div>
    <div class="avatar"><svg width="20" height="20" viewBox="0 0 20 20" fill="#b0b0b0"><circle cx="10" cy="6" r="5"/><path d="M1 20c0-6 4-8 9-8s9 2 9 8z"/></svg></div>
    <div class="caret"></div>
  </div>

  <nav class="categories">
    <div class="category cat-zoo" role="img" aria-label="Photo of a tiger">
      <svg class="slide-arrow prev" width="14" height="24" viewBox="0 0 14 24" fill="none" stroke="#222" stroke-width="3"><polyline points="12,2 2,12 12,22"/></svg>
      <div class="category-label">ZOO</div>
    </div>
    <div class="category cat-exhibition" role="img" aria-label="Photo of a lit sculpture in an exhibition"><div class="category-label">EXHIBITION</div></div>
    <div class="category cat-museum" role="img" aria-label="Photo of a golden museum statue"><div class="category-label">MUSEUM</div></div>
    <div class="category cat-monuments" role="img" aria-label="Photo of an iron tower against the sky"><div class="category-label">MONUMENTS</div></div>
    <div class="category cat-parks" role="img" aria-label="Photo of a park with trees and benches">
      <svg class="slide-arrow next" width="14" height="24" viewBox="0 0 14 24" fill="none" stroke="#222" stroke-width="3"><polyline points="2,2 12,12 2,22"/></svg>
      <div class="category-label">PARKS</div>
    </div>
  </nav>

  <section class="assistant">
    <h1>Find in one click</h1>
    <div class="weather">
      <svg width="34" height="34" viewBox="0 0 34 34" stroke="var(--sun)" stroke-width="2" fill="var(--sun)"><circle cx="17" cy="17" r="7"/><g stroke-linecap="round"><line x1="17" y1="1" x2="17" y2="6"/><line x1="17" y1="28" x2="17" y2="33"/><line x1="1" y1="17" x2="6" y2="17"/><line x1="28" y1="17" x2="33" y2="17"/><line x1="5.5" y1="5.5" x2="9" y2="9"/><line x1="25" y1="25" x2="28.5" y2="28.5"/><line x1="5.5" y1="28.5" x2="9" y2="25"/><line x1="25" y1="9" x2="28.5" y2="5.5"/></g></svg>
      16°c
    </div>
    <p class="intro one">Exhibitions, museums, monuments, zoos?</p>
    <p class="intro two">Tell us what you like, we will tell you where to go!</p>

    <div class="criteria">
      <div class="criterion c-date">
        <svg width="38" height="38" viewBox="0 0 38 38" fill="none" stroke="#222" stroke-width="2.5"><rect x="3" y="6" width="32" height="29"/><line x1="3" y1="13" x2="35" y2="13"/><line x1="11" y1="2" x2="11" y2="9"/><line x1="27" y1="2" x2="27" y2="9"/><g fill="#222" stroke="none"><rect x="8" y="17" width="5" height="4"/><rect x="16" y="17" width="5" height="4"/><rect x="24" y="17" width="5" height="4"/><rect x="8" y="24" width="5" height="4"/><rect x="16" y="24" width="5" height="4"/><rect x="24" y="24" width="5" height="4"/></g></svg>
        <span class="value">SATURDAY 14 DECEMBER</span>
      </div>
      <div class="criterion c-time">
        <svg width="40" height="40" viewBox="0 0 40 40" fill="none" stroke="#222" stroke-width="2.5"><circle cx="20" cy="20" r="17"/><polyline points="20,10 20,20 25,25"/></svg>
        <span class="value">11:00 AM</span>
      </div>
      <div class="criterion c-place">
        <svg width="34" height="44" viewBox="0 0 34 44"><path d="M17 2C8.7 2 2 8.5 2 16.6 2 27 17 42 17 42s15-15 15-25.4C32 8.5 25.3 2 17 2z" fill="#222"/><circle cx="17" cy="16" r="6" fill="#fff"/></svg>
        <span class="value">PARIS<small>FRANCE</small></span>
      </div>
    </div>

    <div class="cta">WHAT DO U WANT ?</div>
    <div class="go">Go</div>
  </section>

  <div class="more-strip"><span>PLUS <i></i></span></div>
  <footer class="site-footer">Copyright 2014 &nbsp; VERMALO</footer>
</main>
</body>
</html>
```